Door Sticker for Loyalty Rewards App

We need to make stickers that will go on the door of the merchants who are part of the Quiver app.

I have attached the Quiver logo, our colours and examples of other door stickers.

Target Market(s)

Millennials

Colors

Designer to choose colors to be used in the design.

Requirements
Must have
• We would like the Quiver logo as the biggest part of the sticker with the text "Effortless Rewards Available Here" and our URL: www.TrulyQuiverTime.com (you can drop the www if you want).
• Must use the Quiver colours.

```html
<!DOCTYPE html>
<html lang="en">
<head>
<meta charset="utf-8">
<title>Quiver Door Stickers</title>
<link href="https://fonts.googleapis.com/css2?family=Arimo:wght@700&display=swap" rel="stylesheet">
<style>
  :root {
    --bg: #ffffff;
    --heading: #8a4bb0;
    --brand-navy: #2b2768;
    --brand-mark: #6a3aa6;
    --url: #1a1a1a;
    --edge-pink: #f0198a;
    --edge-purple: #5b3a9b;
    --edge-blue: #12a7e4;
  }
  html, body {
    margin: 0;
    padding: 0;
    overflow: hidden;
    background: var(--bg);
  }
  .canvas {
    position: relative;
    width: 1200px;
    height: 627px;
    overflow: hidden;
    background: var(--bg);
    font-family: "Arimo", Arial, sans-serif;
    font-weight: 700;
  }
  .sticker-frames {
    position: absolute;
    inset: 0;
  }
  .sticker-content {
    position: absolute;
    display: flex;
    flex-direction: column;
    align-items: center;
    text-align: center;
  }
  .sticker-content--rounded { left: 190px; top: 150px; width: 310px; }
  .sticker-content--leaf { left: 678px; top: 168px; width: 342px; }
  .tagline {
    margin: 0;
    color: var(--heading);
    font-size: 21px;
    line-height: 1.2;
  }
  .brand-mark {
    width: 112px;
    height: 112px;
    margin-top: 28px;
    background: var(--brand-mark);
    border-radius: 6px;
  }
  .sticker-content--leaf .brand-mark { margin-top: 20px; }
  .brand-name {
    margin: 8px 0 0;
    color: var(--brand-navy);
    font-size: 38px;
    line-height: 1;
    letter-spacing: -0.5px;
  }
  .site-url {
    margin: 40px 0 0;
    color: var(--url);
    font-size: 16px;
  }
  .sticker-content--leaf .site-url { margin-top: 26px; }
</style>
</head>
<body>
<main class="canvas">
  <svg class="sticker-frames" width="1200" height="627" viewBox="0 0 1200 627" aria-hidden="true">
    <defs>
      <linearGradient id="edge-rounded" x1="190" y1="492" x2="500" y2="130" gradientUnits="userSpaceOnUse">
        <stop offset="0" stop-color="var(--edge-pink)" style="stop-color: var(--edge-pink)"/>
        <stop offset="0.55" stop-color="#8b3f99" style="stop-color: var(--edge-purple)"/>
        <stop offset="1" stop-color="#12a7e4" style="stop-color: var(--edge-blue)"/>
      </linearGradient>
      <linearGradient id="edge-leaf" x1="678" y1="482" x2="1020" y2="140" gradientUnits="userSpaceOnUse">
        <stop offset="0" stop-color="#f0198a" style="stop-color: var(--edge-pink)"/>
        <stop offset="0.55" stop-color="#5b3a9b" style="stop-color: var(--edge-purple)"/>
        <stop offset="1" stop-color="#12a7e4" style="stop-color: var(--edge-blue)"/>
      </linearGradient>
    </defs>
    <rect class="frame frame--rounded" x="190" y="131" width="310" height="362" rx="24" fill="#fff" stroke="url(#edge-rounded)" stroke-width="7"/>
    <path class="frame frame--leaf" d="M678 482 L678 190 Q678 141 727 141 L1020 141 L1020 433 Q1020 482 971 482 Z" fill="#fff" stroke="url(#edge-leaf)" stroke-width="7" stroke-linejoin="miter"/>
  </svg>

  <section class="sticker-content sticker-content--rounded">
    <p class="tagline">Effortless Rewards<br>Available Here</p>
    <div class="brand-mark"></div>
    <p class="brand-name">Quiver</p>
    <p class="site-url">www.TrulyQuiverTime.com</p>
  </section>

  <section class="sticker-content sticker-content--leaf">
    <p class="tagline">Effortless Rewards<br>Available Here</p>
    <div class="brand-mark"></div>
    <p class="brand-name">Quiver</p>
    <p class="site-url">www.TrulyQuiverTime.com</p>
  </section>
</main>
</body>
</html>
```